Crane Ledger claims recovery services

Its a new company in Dubai UAE. The company activity is debt management, debt collection, loans settlements and restructuring. The company involved in any business or sector requires debt management including government entities, Medical & Health care sector, Banks & finance companies, SME's and commercial business.

Target Market(s)

government entities, Medical & Health care sector, Banks & finance companies, SME's and commercial business.

Industry/Entity Type

Financial Service

Number of Pages Required

5+ page

Requirements
Must have
• Focus on the services not the team and clients
Should not have
• Colorful . Shouldn't have Client testimonial and our clients

```html
<!DOCTYPE html>
<html lang="en">
<head>
<meta charset="utf-8">
<title>Crane Ledger — Claims Recovery Services</title>
<link rel="stylesheet" href="https://fonts.googleapis.com/css2?family=Cinzel:wght@400;600&family=Lato:wght@400;700&display=swap">
<style>
:root{
  --navy:#1f4b73;
  --navy-dark:#173b5c;
  --ink:#1a1a1a;
  --text:#333;
  --grey-bg:#f2f2f2;
  --nav-top:#8c8c8c;
  --nav-bot:#5e5e5e;
  --dark-band:#14202e;
  --footer:#0d0d0d;
  --copy-bar:#264c73;
  --white:#fff;
}
*{box-sizing:border-box;margin:0;padding:0}
html,body{width:669px;height:1200px;overflow:hidden}
body{position:relative;background:var(--white);font-family:"Lato",Arial,sans-serif;color:var(--text)}
.abs{position:absolute}

/* header */
.site-header{left:0;top:0;width:669px;height:53px;background:var(--white)}
.brand{left:55px;top:14px;display:flex;align-items:center;gap:7px}
.brand-mark{width:18px;height:18px;background:var(--navy)}
.brand-name{font-family:"Cinzel",Georgia,serif;font-size:16px;font-weight:600;color:var(--navy);letter-spacing:.5px}
.contact-item{top:17px;display:flex;align-items:center;gap:7px;font-size:8.5px;color:var(--ink)}

/* nav */
.main-nav{left:0;top:53px;width:669px;height:25px;background:linear-gradient(var(--nav-top),var(--nav-bot));display:flex;padding-left:55px}
.nav-item{height:25px;display:flex;align-items:center;justify-content:center;font-family:"Cinzel",Georgia,serif;font-size:8px;color:var(--white);border-right:1px solid rgba(255,255,255,.2);letter-spacing:.3px}
.nav-item.active{background:var(--navy-dark)}
.nav-item:last-child{border-right:0}

/* hero */
.hero{left:0;top:78px;width:669px;height:287px;background:linear-gradient(115deg,#9db4d8 0%,#dfe7f3 45%,#f3f6fb 60%,#a8bddc 100%)}
.hero-caption{left:55px;top:155px;width:310px;height:47px;background:#111;clip-path:polygon(0 0,91% 0,100% 100%,0 100%);padding:5px 0 0 8px;font-family:"Cinzel",Georgia,serif;font-size:13.5px;line-height:20px;color:var(--white);letter-spacing:.4px}
.hero-dots{left:311px;top:263px;display:flex;gap:5px}
.hero-dots span{width:8px;height:8px;border-radius:50%;background:#1d2f45;border:1px solid #fff}

/* section headings */
.section-title{left:0;width:669px;text-align:center;font-family:"Cinzel",Georgia,serif;font-size:17px;font-weight:400;color:var(--ink);letter-spacing:.3px}
.section-title em{font-style:normal;color:var(--navy)}
.divider{height:8px}
.divider::before{content:"";position:absolute;left:0;right:0;top:3.5px;height:1px;background:var(--navy)}
.divider::after{content:"";position:absolute;left:calc(50% - 3.5px);top:0;width:7px;height:7px;border-radius:50%;background:var(--grey-bg);border:1px solid var(--navy)}

/* welcome */
.welcome{left:0;top:365px;width:669px;height:204px;background:var(--grey-bg)}
.welcome-text{left:60px;top:69px;width:549px;text-align:center;font-size:6.9px;line-height:13.6px;color:var(--ink)}
.pillar{top:121px;display:flex;gap:11px}
.pillar-icon{width:52px;height:52px;border-radius:50%;background:var(--navy);border:4px solid #e4e4e4;box-shadow:0 1px 3px rgba(0,0,0,.3);display:flex;align-items:center;justify-content:center;flex:none}
.pillar h3{font-family:"Cinzel",Georgia,serif;font-size:11px;font-weight:400;color:var(--ink);margin:2px 0 4px}
.pillar p{font-size:7px;line-height:12px;color:var(--text);width:112px}
.pillar p b{color:var(--ink)}
.pillar-sep{top:124px;width:1px;height:48px;background:#dcdcdc}

/* services */
.services{left:0;top:569px;width:669px;height:308px;background:radial-gradient(ellipse at 50% 40%,#2a3f58 0%,var(--dark-band) 70%)}
.services .section-title{color:var(--white)}
.services .divider::after{background:#1f3046;border-color:#9fb2c8}
.services .divider::before{background:#9fb2c8}
.card{top:68px;width:107px;height:208px;background:var(--white);border-bottom:3px solid var(--navy)}
.card-photo{width:107px;height:92px}
.card-badge{left:45px;top:84px;width:17px;height:17px;border-radius:50%;background:var(--white);border:2px solid var(--navy)}
.card h4{position:absolute;top:104px;left:0;width:107px;text-align:center;font-family:"Cinzel",Georgia,serif;font-size:10px;font-weight:400;line-height:10.5px;color:var(--ink)}
.card p{position:absolute;top:135px;left:5px;width:97px;text-align:center;font-size:6.8px;line-height:10.6px;color:var(--ink)}
.card-plus{left:45px;bottom:-3px;width:17px;height:9px;border-radius:9px 9px 0 0;background:var(--navy);color:#fff;font-size:9px;line-height:10px;text-align:center;font-weight:700}

/* covering */
.covering{left:0;top:877px;width:669px;height:269px;background:var(--grey-bg)}
.covering-map{left:0;top:0}
.sector-label{font-family:"Cinzel",Georgia,serif;font-size:8px;color:var(--ink);text-align:center;line-height:10px;letter-spacing:.5px}
.center-name{left:259px;top:215px;width:150px;text-align:center;font-family:"Cinzel",Georgia,serif;font-size:12px;font-weight:600;color:var(--navy)}

/* footer */
.site-footer{left:0;top:1146px;width:669px;height:30px;background:var(--footer);color:var(--white);font-size:8.5px}
.foot-item{top:9px;display:flex;align-items:center;gap:6px}
.social{top:7px;display:flex;gap:4px;left:540px}
.social span{width:16px;height:16px;border-radius:50%;background:var(--white)}
.copyright{left:0;top:1176px;width:669px;height:24px;background:var(--copy-bar);color:#e8eef5;font-size:7.5px;text-align:center;line-height:24px}
</style>
</head>
<body>

<header class="site-header abs">
  <div class="brand abs"><span class="brand-mark"></span><span class="brand-name">Crane Ledger</span></div>
  <div class="contact-item abs" style="left:404px">
    <svg width="18" height="18" viewBox="0 0 18 18"><circle cx="9" cy="9" r="8" fill="none" stroke="#1f4b73" stroke-width="1.6"/><path d="M6 5.5l1.8-.5 1 2.3-1.1.8a5 5 0 0 0 2.2 2.2l.8-1.1 2.3 1-.5 1.8c-3.6.3-6.8-2.9-6.5-6.5z" fill="#1f4b73"/></svg>
    555-014-2290
  </div>
  <div class="contact-item abs" style="left:512px">
    <svg width="18" height="18" viewBox="0 0 18 18"><circle cx="9" cy="9" r="8" fill="none" stroke="#1f4b73" stroke-width="1.6"/><rect x="5" y="6" width="8" height="6" fill="#1f4b73"/><path d="M5 6l4 3.3L13 6" fill="none" stroke="#fff" stroke-width=".9"/></svg>
    info@craneledger.com
  </div>
</header>

<nav class="main-nav abs">
  <div class="nav-item active" style="width:82px">Home</div>
  <div class="nav-item" style="width:123px">About Us</div>
  <div class="nav-item" style="width:138px">Our Services</div>
  <div class="nav-item" style="width:104px">Team</div>
  <div class="nav-item" style="width:112px">Contact Us</div>
</nav>

<section class="hero abs" role="img" aria-label="Close-up photo of a calculator keypad, a ballpoint pen and a printed financial chart in blue tones">
  <div class="hero-caption abs">Managing your money<br>recovering your relationships</div>
  <div class="hero-dots abs"><span></span><span></span><span></span><span></span></div>
</section>

<section class="welcome abs">
  <h2 class="section-title abs" style="top:24px">Welcome to <em>Crane Ledger.</em></h2>
  <div class="divider abs" style="top:46px;left:206px;width:257px"></div>
  <p class="welcome-text abs">We are a Claims Recovery and Debt Management Services company based in Dubai, United Arab Emirates. The Crane Ledger team handles a comprehensive range of debt recoveries, such as invoices; insurance payments; supplier and rent payments; and personal and business loans, for individuals and businesses across an array of industries. Crane Ledger was founded on traditional values, and we're proud of our personal approach.</p>

  <div class="pillar abs" style="left:62px">
    <div class="pillar-icon"><svg width="30" height="30" viewBox="0 0 30 30" fill="none" stroke="#fff" stroke-width="2.2"><circle cx="14" cy="16" r="11"/><circle cx="14" cy="16" r="6.5"/><circle cx="14" cy="16" r="2" fill="#fff"/><path d="M14 16L26 4M22 4h4v4"/></svg></div>
    <div><h3>Mission</h3><p>Crane Ledger is a leading Debt Management and Claims Recovery Services..... <b>[ + ]</b></p></div>
  </div>
  <div class="pillar-sep abs" style="left:240px"></div>
  <div class="pillar abs" style="left:257px">
    <div class="pillar-icon"><svg width="32" height="22" viewBox="0 0 32 22"><path d="M1 11C6 3 26 3 31 11 26 19 6 19 1 11z" fill="#fff"/><circle cx="16" cy="11" r="6" fill="#1f4b73"/><circle cx="16" cy="11" r="2.6" fill="#fff"/></svg></div>
    <div><h3>Vision</h3><p>Our success is built on traditions of trust, valued and respect.....<b>[+]</b></p></div>
  </div>
  <div class="pillar-sep abs" style="left:436px"></div>
  <div class="pillar abs" style="left:452px">
    <div class="pillar-icon"><svg width="32" height="24" viewBox="0 0 32 24" fill="none" stroke="#fff" stroke-width="2" stroke-linejoin="round"><path d="M2 6l6-3 5 2M30 6l-6-3-7 3-4 4 3 1 4-2 7 6"/><path d="M2 6v9l3 2 4 4 2-1 3 2 2-1 3 1 6-6"/></svg></div>
    <div><h3>Values</h3><p>At Crane Ledger, our values are born of time-honoured traditions.... <b>[ + ]</b></p></div>
  </div>
</section>

<section class="services abs">
  <h2 class="section-title abs" style="top:22px">Our Services</h2>
  <div class="divider abs" style="top:45px;left:270px;width:129px"></div>

  <article class="card abs" style="left:55px">
    <div class="card-photo" role="img" aria-label="Photo of business people reviewing a chart on a tablet" style="background:linear-gradient(135deg,#3a4a5c,#9aa8b8)"></div>
    <span class="card-badge abs"></span>
    <h4>Recovery<br>Solutions</h4>
    <p>Our experience has taught us that when it comes to recovery, it always pays to find the most amicable solution,</p>
    <span class="card-plus abs">+</span>
  </article>
  <article class="card abs" style="left:168px">
    <div class="card-photo" role="img" aria-label="Photo of a calculator and pen on a financial report" style="background:linear-gradient(135deg,#7f9cc6,#dce5f2)"></div>
    <span class="card-badge abs"></span>
    <h4>Debt<br>Management</h4>
    <p>At Crane Ledger, we pull together our wisdom and expertise to make debt work for you.</p>
    <span class="card-plus abs">+</span>
  </article>
  <article class="card abs" style="left:281px">
    <div class="card-photo" role="img" aria-label="Photo of a magnifying glass over printed words about debt settlement" style="background:linear-gradient(135deg,#f2f4f7,#9fb6d4)"></div>
    <span class="card-badge abs"></span>
    <h4>Debt<br>Settlement</h4>
    <p>Lorem ipsum dolor sit amet, consectetuer adipiscing elit, sed diam nonummy nibh euismod tincidunt ut laoreet dolore</p>
    <span class="card-plus abs">+</span>
  </article>
  <article class="card abs" style="left:394px">
    <div class="card-photo" role="img" aria-label="Photo of business people shaking hands in an office" style="background:linear-gradient(135deg,#c9d6e6,#3d4f66)"></div>
    <span class="card-badge abs"></span>
    <h4 style="top:110px">Outsourcing</h4>
    <p>Lorem ipsum dolor sit amet, consectetuer adipiscing elit, sed diam nonummy nibh euismod tincidunt ut laoreet dolore</p>
    <span class="card-plus abs">+</span>
  </article>
  <article class="card abs" style="left:507px">
    <div class="card-photo" role="img" aria-label="Photo of hands typing on a keyboard" style="background:linear-gradient(135deg,#e8eef6,#5d86b5)"></div>
    <span class="card-badge abs"></span>
    <h4>Interactive<br>Online Access</h4>
    <p>Lorem ipsum dolor sit amet, consectetuer adipiscing elit, sed diam nonummy nibh euismod tincidunt ut laoreet dolore</p>
    <span class="card-plus abs">+</span>
  </article>
</section>

<section class="covering abs">
  <h2 class="section-title abs" style="top:22px">We are <em>covering</em></h2>
  <div class="divider abs" style="top:45px;left:230px;width:209px"></div>

  <svg class="covering-map abs" width="669" height="269" viewBox="0 0 669 269">
    <defs>
      <linearGradient id="arcShade" x1="0" y1="0" x2="0" y2="1">
        <stop offset="0" stop-color="#d6d6d6"/><stop offset="1" stop-color="#f2f2f2"/>
      </linearGradient>
      <filter id="iconShadow" x="-30%" y="-30%" width="160%" height="160%"><feDropShadow dx="0" dy="1" stdDeviation="1.2" flood-opacity=".3"/></filter>
    </defs>
    <path d="M208 269A126 126 0 0 1 460 269H440A106 106 0 0 0 228 269Z" fill="url(#arcShade)"/>
    <path d="M228 269A106 106 0 0 1 440 269Z" fill="#fafafa"/>
    <g stroke="#b8c4d0" stroke-width="1">
      <line x1="222" y1="216" x2="190" y2="201"/>
      <line x1="263" y1="169" x2="242" y2="144"/>
      <line x1="325" y1="152" x2="325" y2="133"/>
      <line x1="387" y1="169" x2="408" y2="144"/>
      <line x1="430" y1="216" x2="460" y2="200"/>
    </g>
    <g fill="#4a87b5" stroke="#fff" stroke-width="1">
      <circle cx="222" cy="216" r="3"/><circle cx="263" cy="169" r="3"/><circle cx="325" cy="152" r="3"/><circle cx="387" cy="169" r="3"/><circle cx="430" cy="216" r="3"/>
    </g>
    <g filter="url(#iconShadow)" fill="#fff" stroke="#e3e3e3" stroke-width="1.5">
      <circle cx="175" cy="201" r="16"/><circle cx="237" cy="133" r="16"/><circle cx="325" cy="110" r="16"/><circle cx="413" cy="133" r="16"/><circle cx="474" cy="195" r="16"/>
    </g>
    <g class="icon-government" fill="#1a1a1a"><path d="M166 195l9-5 9 5z"/><rect x="167" y="196" width="16" height="1.5"/><rect x="168" y="198" width="2" height="7"/><rect x="172" y="198" width="2" height="7"/><rect x="176" y="198" width="2" height="7"/><rect x="180" y="198" width="2" height="7"/><rect x="166" y="205.5" width="18" height="2"/></g>
    <g class="icon-bank" fill="#1a1a1a"><rect x="228" y="125" width="18" height="4"/><rect x="229" y="130" width="16" height="10" fill="none" stroke="#1a1a1a" stroke-width="2"/><rect x="234" y="133" width="6" height="7"/></g>
    <g class="icon-shop" fill="#1a1a1a"><rect x="316" y="101" width="18" height="5"/><rect x="317" y="107" width="16" height="11" fill="none" stroke="#1a1a1a" stroke-width="2"/><rect x="320" y="110" width="4" height="8"/><rect x="326" y="110" width="4" height="4"/></g>
    <g class="icon-health"><rect x="404" y="128" width="18" height="13" rx="2" fill="#1a1a1a"/><rect x="409" y="125" width="8" height="4" fill="none" stroke="#1a1a1a" stroke-width="1.5"/><circle cx="413" cy="134.5" r="4.5" fill="#fff"/><path d="M411.5 134.5h3M413 133v3" stroke="#1a1a1a" stroke-width="1.3"/></g>
    <g class="icon-commercial" fill="#1a1a1a"><rect x="466" y="190" width="6" height="14"/><rect x="473" y="186" width="7" height="18"/><rect x="481" y="194" width="4" height="10"/><rect x="464" y="204" width="22" height="1.5"/></g>
  </svg>

  <div class="sector-label abs" style="left:79px;top:193px;width:80px">Government<br>entities</div>
  <div class="sector-label abs" style="left:163px;top:127px;width:60px">Banks</div>
  <div class="sector-label abs" style="left:295px;top:80px;width:60px">SME</div>
  <div class="sector-label abs" style="left:425px;top:120px;width:90px">Health Care</div>
  <div class="sector-label abs" style="left:487px;top:187px;width:90px">Commercial<br>industrial</div>
  <div class="center-name abs">Crane Ledger</div>
</section>

<footer class="site-footer abs">
  <div class="foot-item abs" style="left:55px">
    <svg width="9" height="13" viewBox="0 0 9 13"><path d="M4.5 0A4.5 4.5 0 0 0 0 4.5C0 8 4.5 13 4.5 13S9 8 9 4.5A4.5 4.5 0 0 0 4.5 0z" fill="#fff"/><circle cx="4.5" cy="4.5" r="1.8" fill="#0d0d0d"/></svg>
    Lorem ipsum dolor sit amet, adipiscing elit
  </div>
  <div class="foot-item abs" style="left:246px">
    <svg width="10" height="11" viewBox="0 0 10 11"><path d="M1 1.5L3.5 1 5 4 3.6 5a6 6 0 0 0 2.6 2.6L7 6.3l3 1.4-.6 2.6C4.6 10.6.4 6.4 1 1.5z" fill="#fff"/></svg>
    555-014-2290
  </div>
  <div class="foot-item abs" style="left:334px">
    <svg width="12" height="9" viewBox="0 0 12 9"><rect width="12" height="9" fill="#fff"/><path d="M0 0l6 5 6-5" fill="none" stroke="#0d0d0d" stroke-width="1"/></svg>
    info@craneledger.com
  </div>
  <div class="social abs"><span></span><span></span><span></span><span></span></div>
</footer>
<div class="copyright abs">Copyright 2016 Craneledger. All rights reserved.</div>

</body>
</html>
```